Orvo Lark Info Graphic Design

We need an update to our current infographic design. It should be modern and readable and follow our branding at www.orvo-lark.com.

```html
<!DOCTYPE html>
<html lang="en">
<head>
<meta charset="utf-8">
<title>Orvo Lark – Market Snapshot</title>
<link href="https://fonts.googleapis.com/css2?family=Anton&family=Oswald:wght@700&family=Open+Sans:wght@300;400;600;700&display=swap" rel="stylesheet">
<style>
  :root {
    --stage: #2b2b2b;
    --brand-blue: #2f5a97;
    --title-blue: #2a4f8c;
    --deep-blue: #3a5494;
    --ink: #2b2b2b;
    --hot-red: #e8202a;
    --teal: #1fa39a;
    --paper-top: #f7f6fb;
    --paper-mid: #f6e6ec;
    --paper-peach: #f8e9df;
    --paper-bottom: #8fb2e0;
  }
  * { box-sizing: border-box; margin: 0; padding: 0; }
  html, body { width: 1200px; height: 1088px; overflow: hidden; background: var(--stage); }
  .canvas { position: relative; width: 1200px; height: 1088px; }
  .flyer {
    position: absolute; left: 210px; top: 12px; width: 780px; height: 1064px; overflow: hidden;
    font-family: "Open Sans", sans-serif; color: var(--ink);
    background: linear-gradient(180deg, var(--paper-top) 0%, #f5eef6 30%, var(--paper-mid) 55%, var(--paper-peach) 72%, #f1cfe0 86%, var(--paper-bottom) 100%);
  }
  .abs { position: absolute; }
  .brand { left: 30px; top: 30px; display: flex; align-items: center; gap: 18px; }
  .brand-dot { width: 64px; height: 64px; border-radius: 50%; background: var(--brand-blue); }
  .brand-name { font-size: 24px; letter-spacing: 7px; color: var(--brand-blue); font-weight: 400; }
  .brand-tagline { font-size: 12px; color: #555; margin-top: 6px; }
  .headline {
    left: 33px; top: 106px; font-family: "Oswald", sans-serif; font-weight: 700;
    font-size: 42px; line-height: 44px; color: var(--title-blue); letter-spacing: 1px;
    text-shadow: 2px 2px 2px rgba(0,0,0,.35); text-align: center;
  }
  .jet-photo {
    left: 400px; top: 40px; width: 311px; height: 72px; border-radius: 40px 60px 30px 30px;
    background: linear-gradient(180deg, #ffffff 0%, #e4e6ea 60%, #b9bec6 100%);
  }
  .hang { left: 0; top: 0; }
  .market-disc {
    left: 342px; top: 527px; width: 366px; height: 366px; border-radius: 50%;
    background: var(--deep-blue); box-shadow: -6px 6px 14px rgba(0,0,0,.35);
  }
  .stat-number { left: 398px; top: 352px; font-size: 142px; font-weight: 300; color: var(--brand-blue); line-height: 1; letter-spacing: -4px; }
  .stat-label { left: 550px; top: 364px; font-size: 28px; font-weight: 700; color: var(--brand-blue); line-height: 37px; }
  .metric-label { left: 66px; font-size: 20px; color: #333; }
  .metric-box {
    left: 66px; width: 169px; height: 43px; background: var(--brand-blue); color: #fff;
    font-size: 19px; display: flex; align-items: center; justify-content: center;
  }
  .deliveries { left: 56px; top: 618px; width: 175px; text-align: center; font-size: 19px; line-height: 27px; color: #333; }
  .handshake { left: 60px; top: 688px; width: 159px; height: 90px; border-radius: 45px; background: linear-gradient(180deg, #4a74ad, #2f5a97); }
  .hot-deals {
    left: 30px; top: 866px; font-family: "Anton", sans-serif; font-size: 30px; color: var(--hot-red);
    text-decoration: underline; text-decoration-thickness: 2px; text-underline-offset: 3px;
  }
  .deal { width: 240px; text-align: center; top: 918px; }
  .plane-icon { display: block; width: 112px; height: 30px; margin: 0 auto 12px; border-radius: 15px 40px 6px 6px; background: var(--teal); }
  .deal-code { font-size: 35px; font-weight: 700; line-height: 1; color: #222; }
  .deal-seller { font-size: 12.5px; font-weight: 700; letter-spacing: .4px; color: #222; margin-top: 4px; }
  .contact { top: 1018px; display: flex; align-items: center; gap: 6px; font-size: 22px; color: #222; }
  .contact svg { flex: none; }
</style>
</head>
<body>
<div class="canvas">
  <div class="flyer">
    <div class="abs brand">
      <div class="brand-dot"></div>
      <div>
        <div class="brand-name">ORVO LARK</div>
        <div class="brand-tagline">Midsize Focused. Client Driven.</div>
      </div>
    </div>

    <div class="abs headline">MARKET SHNAPSHOT<br>MAY - AUGUST 2014</div>

    <div class="abs jet-photo" role="img" aria-label="Photo of a white business jet in flight"></div>

    <div class="abs market-disc"></div>

    <svg class="abs hang" width="780" height="1064" viewBox="0 0 780 1064">
      <path d="M546 112 Q548 140 550 178" stroke="#2f5a97" stroke-width="2" fill="none"/>
      <path d="M470 205 C470 175 520 165 545 185 C565 160 620 170 622 205 C660 205 665 260 630 270 C640 305 590 325 560 305 C545 330 480 330 470 305 C420 310 400 265 430 250 C405 230 430 200 470 205 Z"
            fill="#fff" stroke="#2e2a8a" stroke-width="4"/>
      <text x="530" y="275" transform="rotate(-12 530 260)" text-anchor="middle"
            font-family="Anton, sans-serif" font-size="44" fill="#e8202a">FOR SALE</text>
      <g fill="#2f5a97">
        <rect x="70" y="345" width="16" height="42"/>
        <rect x="92" y="325" width="16" height="62"/>
        <rect x="114" y="340" width="16" height="47"/>
        <rect x="136" y="322" width="16" height="65"/>
        <rect x="158" y="308" width="16" height="79"/>
        <path d="M66 334 L100 304 L125 322 L170 284 L162 277 L190 270 L184 298 L177 291 L125 336 L100 318 L73 342 Z"/>
      </g>
    </svg>

    <div class="abs stat-number">37</div>
    <div class="abs stat-label"># OF<br>AIRCRAFT<br>FOR SALE</div>

    <div class="abs metric-label" style="top:244px">SUPPLY TREAD</div>
    <div class="abs metric-label" style="top:404px">PRICING TREAD</div>
    <div class="abs metric-box" style="top:443px">$$$$$$$$$</div>
    <div class="abs metric-label" style="top:509px">AVERAGE PRICE</div>
    <div class="abs metric-box" style="top:546px">$5,900,000</div>
    <div class="abs deliveries">USED AIRCRAFT<br>DELIVERIES</div>
    <div class="abs handshake" role="img" aria-label="Handshake icon illustration"></div>

    <div class="abs hot-deals">HOT DEAILS</div>

    <div class="abs deal" style="left:-8px">
      <span class="plane-icon" role="img" aria-label="Teal airplane icon"></span>
      <div class="deal-code">750-0037</div>
      <div class="deal-seller">MERIDIAN BUSINESS JETS</div>
    </div>
    <div class="abs deal" style="left:265px">
      <span class="plane-icon" role="img" aria-label="Teal airplane icon"></span>
      <div class="deal-code">750-0037</div>
      <div class="deal-seller">MERIDIAN BUSINESS JETS</div>
    </div>
    <div class="abs deal" style="left:516px">
      <span class="plane-icon" role="img" aria-label="Teal airplane icon"></span>
      <div class="deal-code">750-0037</div>
      <div class="deal-seller">MERIDIAN BUSINESS JETS</div>
    </div>

    <div class="abs contact" style="left:22px">
      <svg width="26" height="26" viewBox="0 0 26 26"><circle cx="13" cy="13" r="11.5" fill="none" stroke="#222" stroke-width="2"/><path d="M8 7 l3 -1 2 4 -2 1.5 c1 2 2 3 4 4 l1.5 -2 4 2 -1 3 c-6 0 -11.5 -5.5 -11.5 -11.5z" fill="#222"/></svg>
      <span>512-555-0148</span>
    </div>
    <div class="abs contact" style="left:225px">
      <svg width="38" height="26" viewBox="0 0 38 26"><rect x="1" y="1" width="36" height="24" fill="none" stroke="#222" stroke-width="2"/><path d="M1 1 L19 15 L37 1 M1 25 L14 11 M37 25 L24 11" stroke="#222" stroke-width="2" fill="none"/></svg>
      <span>sales@orvo-lark.com</span>
    </div>
    <div class="abs contact" style="left:502px">
      <svg width="26" height="26" viewBox="0 0 26 26" fill="none" stroke="#222" stroke-width="2"><circle cx="13" cy="13" r="11.5"/><ellipse cx="13" cy="13" rx="5" ry="11.5"/><path d="M1.5 13 H24.5 M3.5 7 H22.5 M3.5 19 H22.5"/></svg>
      <span>www.orvo-lark.com</span>
    </div>
  </div>
</div>
</body>
</html>
```